Large multi-office optometry business opening a Dry Eye Spa and needs sign.

Business name/sign info: Brenwick Dry Eye Institute, (555) 362-4817
Backlit pole sign at office entrance on a very busy street
Sign dimensions: 53" tall x 136.5" wide
State of the art Dry Eye Spa for treatment of all forms of dry eye and ocular surface disease. Also, have aesthetics treatments (IPL, Low Level Light Treatment, etc.)

Target Market(s)

People who are suffering from: dryness, burning, foreign body sensation, itching, fluctuating vision, tired eyes, etc.

Industry/Entity Type

Optometry and aesthetics

Colors
0054AA
0677BA
7BADD7
CADEEF
E8F1F8

Requirements
Must have
• Business name, phone number, subliminal message of relief in a glance or short look.
Nice to have
• Cool, relief, soothing sense.
Should not have
• Too much information or too busy.

```html
<!DOCTYPE html>
<html lang="en">
<head>
<meta charset="utf-8">
<title>Brenwick Dry Eye Institute – Pole Sign</title>
<link href="https://fonts.googleapis.com/css2?family=Bebas+Neue&family=Yellowtail&display=swap" rel="stylesheet">
<style>
  :root {
    --page-bg: #e8f1f8;
    --sign-bg: #111111;
    --white-top: #ffffff;
    --white-bottom: #d9d9d9;
    --blue-deep: #1e9bd6;
    --blue-bright: #5fd0f4;
    --script-blue: #4cc3ec;
    --label-white: #f2f2f2;
  }
  html, body {
    margin: 0;
    padding: 0;
    width: 1200px;
    height: 717px;
    overflow: hidden;
    background: var(--page-bg);
  }
  .canvas {
    position: relative;
    width: 1200px;
    height: 717px;
  }
  .sign {
    position: absolute;
    left: 20px;
    top: 137px;
    width: 1160px;
    height: 443px;
    display: block;
  }
  .sign-face { fill: var(--sign-bg); }
  .business-name,
  .business-type,
  .contact-line,
  .service-label {
    font-family: "Bebas Neue", "Oswald", sans-serif;
  }
  .business-name { font-size: 120px; fill: url(#whiteFade); }
  .business-type { font-size: 114px; fill: url(#blueFade); }
  .contact-line { font-size: 64px; fill: url(#whiteFade); }
  .divider-dot { fill: var(--script-blue); }
  .column-rule { stroke: var(--script-blue); stroke-width: 1.5; opacity: .8; }
  .spa-tagline {
    font-family: "Yellowtail", cursive;
    font-size: 38px;
    fill: var(--script-blue);
  }
  .service-label { font-size: 29px; fill: var(--label-white); }
  .service-thumb { stroke: #ffffff; stroke-width: 2; }
</style>
</head>
<body>
<div class="canvas">
  <svg class="sign" viewBox="0 0 1160 443" xmlns="http://www.w3.org/2000/svg" aria-label="Brenwick Dry Eye Institute sign">
    <defs>
      <linearGradient id="whiteFade" x1="0" y1="0" x2="0" y2="1">
        <stop offset="0" stop-color="var(--white-top)"/>
        <stop offset="1" stop-color="var(--white-bottom)"/>
      </linearGradient>
      <linearGradient id="blueFade" x1="0" y1="0" x2="1" y2="0">
        <stop offset="0" stop-color="var(--blue-deep)"/>
        <stop offset="1" stop-color="var(--blue-bright)"/>
      </linearGradient>
      <linearGradient id="thumbConsult" x1="0" y1="0" x2="1" y2="1">
        <stop offset="0" stop-color="#d9a47a"/>
        <stop offset="1" stop-color="#5d7fa6"/>
      </linearGradient>
      <radialGradient id="thumbAnatomy">
        <stop offset="0" stop-color="#e0622e"/>
        <stop offset=".7" stop-color="#c44a2c"/>
        <stop offset="1" stop-color="#eeeeee"/>
      </radialGradient>
      <radialGradient id="thumbEye">
        <stop offset="0" stop-color="#4f7d8e"/>
        <stop offset=".45" stop-color="#8a9a9c"/>
        <stop offset="1" stop-color="#8a5a3e"/>
      </radialGradient>
    </defs>

    <rect class="sign-face" x="0" y="0" width="1160" height="443"/>

    <g class="identity">
      <text class="business-name" x="393" y="164" text-anchor="middle">BRENWICK</text>
      <text class="business-type" x="87" y="248" textLength="601" lengthAdjust="spacingAndGlyphs">DRY EYE INSTITUTE</text>
      <g class="dot-divider">
        <circle class="divider-dot" cx="88" cy="293" r="2.6"/>
        <circle class="divider-dot" cx="115.2" cy="293" r="2.6"/>
        <circle class="divider-dot" cx="142.4" cy="293" r="2.6"/>
        <circle class="divider-dot" cx="169.6" cy="293" r="2.6"/>
        <circle class="divider-dot" cx="196.7" cy="293" r="2.6"/>
        <circle class="divider-dot" cx="223.9" cy="293" r="2.6"/>
        <circle class="divider-dot" cx="251.1" cy="293" r="2.6"/>
        <circle class="divider-dot" cx="278.3" cy="293" r="2.6"/>
        <circle class="divider-dot" cx="305.5" cy="293" r="2.6"/>
        <circle class="divider-dot" cx="332.6" cy="293" r="2.6"/>
        <circle class="divider-dot" cx="359.8" cy="293" r="2.6"/>
        <circle class="divider-dot" cx="387" cy="293" r="2.6"/>
        <circle class="divider-dot" cx="414.2" cy="293" r="2.6"/>
        <circle class="divider-dot" cx="441.4" cy="293" r="2.6"/>
        <circle class="divider-dot" cx="468.5" cy="293" r="2.6"/>
        <circle class="divider-dot" cx="495.7" cy="293" r="2.6"/>
        <circle class="divider-dot" cx="522.9" cy="293" r="2.6"/>
        <circle class="divider-dot" cx="550.1" cy="293" r="2.6"/>
        <circle class="divider-dot" cx="577.3" cy="293" r="2.6"/>
        <circle class="divider-dot" cx="604.4" cy="293" r="2.6"/>
        <circle class="divider-dot" cx="631.6" cy="293" r="2.6"/>
        <circle class="divider-dot" cx="658.8" cy="293" r="2.6"/>
        <circle class="divider-dot" cx="686" cy="293" r="2.6"/>
      </g>
      <text class="contact-line" x="135" y="389" textLength="502" lengthAdjust="spacingAndGlyphs">CONTACT : (555) 362-4817</text>
    </g>

    <line class="column-rule" x1="776" y1="59" x2="776" y2="394"/>

    <g class="services">
      <text class="spa-tagline" x="844" y="78" textLength="224" lengthAdjust="spacingAndGlyphs">State of the art</text>
      <text class="spa-tagline" x="844" y="120">Dry Eye Spa</text>

      <circle class="service-thumb" cx="879" cy="186" r="34" fill="url(#thumbConsult)" role="img" aria-label="Photo of an eye examination with trial frames"/>
      <text class="service-label" x="928" y="182">ALL FORMS</text>
      <text class="service-label" x="928" y="210">OF DRY EYE</text>

      <circle class="service-thumb" cx="879" cy="273" r="34" fill="url(#thumbAnatomy)" role="img" aria-label="Illustration of eye anatomy cross-section"/>
      <text class="service-label" x="928" y="267">OCULAR SURFACE</text>
      <text class="service-label" x="928" y="294">DISEASE</text>

      <circle class="service-thumb" cx="879" cy="359" r="34" fill="url(#thumbEye)" role="img" aria-label="Close-up photo of a blue eye"/>
      <text class="service-label" x="928" y="354">AESTHETICS</text>
      <text class="service-label" x="928" y="381">TREATMENT</text>
    </g>
  </svg>
</div>
</body>
</html>
```